Alaskan medical billing service needs a business card design

We need a business card design for a medical billing service, located in Anchorage, AK. We provide medical claims billing and management to Alaskan medical practices/clinics. We would like to see designs that depict Alaskan Mountain Ranges, or water features, or trees. An outdoorsy feel, perhaps. Not exactly sure.

Industry/Entity Type

Medical

```html
<!DOCTYPE html>
<html lang="en">
<head>
<meta charset="utf-8">
<title>Kenai Claims – Business Card</title>
<link rel="stylesheet" href="https://fonts.googleapis.com/css2?family=Oswald:wght@500;600&family=Tenor+Sans&display=swap">
<style>
  :root {
    --page: #fdfdfd;
    --card: #f3f4f6;
    --brown: #6a4030;
    --ink-grey: #6f6f72;
    --icon-grey: #5a5a5d;
    --shadow: rgba(0, 0, 0, 0.22);
  }
  * { margin: 0; padding: 0; box-sizing: border-box; }
  html, body {
    width: 1200px;
    height: 900px;
    overflow: hidden;
    background: var(--page);
  }
  .canvas {
    position: relative;
    width: 1200px;
    height: 900px;
  }
  .business-card {
    position: absolute;
    left: 168px;
    top: 145px;
    width: 853px;
    height: 520px;
    background: var(--card);
    box-shadow: 3px 4px 6px var(--shadow);
  }
  .brand {
    position: absolute;
    left: 0;
    right: 0;
    top: 130px;
    text-align: center;
    color: var(--brown);
    font-family: "Oswald", sans-serif;
    font-weight: 600;
  }
  .brand-name {
    font-size: 76px;
    line-height: 1;
    letter-spacing: 2px;
    text-transform: uppercase;
  }
  .brand-descriptor {
    margin-top: 14px;
    font-size: 30px;
    line-height: 1;
    letter-spacing: 0.5px;
    text-transform: uppercase;
  }
  .contact-list {
    position: absolute;
    left: 268px;
    top: 296px;
    list-style: none;
  }
  .contact-item {
    display: flex;
    align-items: center;
    height: 39px;
    font-family: "Tenor Sans", sans-serif;
    font-size: 22px;
    color: var(--ink-grey);
  }
  .contact-icon {
    width: 36px;
    height: 36px;
    margin-right: 18px;
    flex: none;
  }
  .service-line {
    position: absolute;
    left: 73px;
    width: 714px;
    top: 464px;
    height: 30px;
    border-top: 2px solid var(--brown);
    border-bottom: 2px solid var(--brown);
    text-align: center;
    font-family: "Tenor Sans", sans-serif;
    font-size: 18.5px;
    line-height: 26px;
    color: var(--brown);
  }
</style>
</head>
<body>
<main class="canvas">
  <section class="business-card">
    <div class="brand">
      <div class="brand-name">Kenai Claims</div>
      <div class="brand-descriptor">Medical Billing Service</div>
    </div>

    <ul class="contact-list">
      <li class="contact-item">
        <svg class="contact-icon" viewBox="0 0 36 36" aria-hidden="true">
          <circle cx="16" cy="20" r="12" fill="none" stroke="var(--icon-grey)" stroke-width="2.5"/>
          <path d="M4 20h24M16 8c-5 6-5 18 0 24M16 8c5 6 5 18 0 24" fill="none" stroke="var(--icon-grey)" stroke-width="2"/>
          <path d="M26 2a6 6 0 0 1 6 6c0 5-6 10-6 10s-6-5-6-10a6 6 0 0 1 6-6z" fill="var(--icon-grey)" stroke="var(--card)" stroke-width="1.5"/>
          <circle cx="26" cy="8" r="2" fill="var(--card)"/>
        </svg>
        <span>Anchorage, AK</span>
      </li>
      <li class="contact-item">
        <svg class="contact-icon" viewBox="0 0 36 36" aria-hidden="true">
          <rect x="8" y="2" width="20" height="33" rx="3" transform="rotate(-12 18 18)" fill="none" stroke="var(--icon-grey)" stroke-width="2.5"/>
          <circle cx="22" cy="30" r="1.8" fill="var(--icon-grey)"/>
        </svg>
        <span>1234456679</span>
      </li>
      <li class="contact-item">
        <svg class="contact-icon" viewBox="0 0 36 36" aria-hidden="true">
          <text x="18" y="27" text-anchor="middle" font-family="Georgia, serif" font-style="italic" font-size="26" fill="var(--icon-grey)">@</text>
        </svg>
        <span>website/blog</span>
      </li>
      <li class="contact-item">
        <svg class="contact-icon" viewBox="0 0 36 36" aria-hidden="true">
          <rect x="2" y="9" width="32" height="20" rx="2" fill="var(--icon-grey)"/>
          <path d="M3 10l15 11 15-11M3 28l11-9M33 28l-11-9" fill="none" stroke="var(--card)" stroke-width="1.5"/>
        </svg>
        <span>Email</span>
      </li>
    </ul>

    <p class="service-line">medical claims billing and management to Alaskan medical practices/clinics</p>
  </section>
</main>
</body>
</html>
```